Rug Cleaning Web Design Project

We need a web design for our cleaning company. We currently have a web page but are not happy with its design. We currently offer fine rug cleaning,upholstery cleaning, and residential and commercial carpet cleanning. We also offer water damage restoration. For our rug cleaning services we offer : Enzyme treatments for pet contamination and odor removal, application of stain protection that is designed for the fine textiles used in rug construction, application of treatments designed to prevent moth damage and pads designed to be used under rugs.Our current web site is harborfreshcare.example. We are intrested in a design with similar information to the web page of Velmora Rug Cleaners INC. We would like to use the colors that are present in our logo that will be uploaded with this description. We would also like this new page to be linked to our other address loomrinsepro.example. We would like the deign to be visually attractive but not "too busy".
Updates

Please include pictures of rugs, or people washing rugs if possible. We do not offer maid type cleaning services. We would not be interested in designs including pictures depicting that type service. Thanks for your hard work on this project.

Dana Whitlow

Industry/Entity Type

Residential

Requirements
Must have
• This page must be viewable on smart phones and tablets.

```html
<!DOCTYPE html>
<html lang="en">
<head>
<meta charset="utf-8">
<meta name="viewport" content="width=device-width, initial-scale=1">
<title>Loom Rinse Pro – Harborfresh Care &amp; Restoration</title>
<link rel="stylesheet" href="https://fonts.googleapis.com/css2?family=Cinzel:wght@400;700&family=Carlito:ital,wght@0,400;0,700;1,400;1,700&family=Mulish:wght@400;700;800&family=Raleway:wght@200;300&display=swap">
<style>
  :root {
    --brand-blue: #1f6fb8;
    --brand-blue-dark: #0f4f92;
    --brand-blue-light: #4f9be0;
    --accent-orange: #f05a14;
    --ink: #1a1a1a;
    --ink-soft: #444;
    --muted: #7a7a7a;
    --rule: #d6d6d6;
    --rug-red: #b0323a;
    --rug-deep: #7c1e2a;
    --sky: #1d4f8f;
    --page: #ffffff;
  }
  * { box-sizing: border-box; margin: 0; padding: 0; }
  html, body { width: 1064px; height: 1200px; overflow: hidden; background: var(--page); }
  body { font-family: "Carlito", "Calibri", sans-serif; color: var(--ink); }
  .canvas { position: relative; width: 1064px; height: 1200px; overflow: hidden; background: var(--page); }

  .backdrop {
    position: absolute; left: 0; top: 0; width: 1064px; height: 600px;
    background:
      linear-gradient(180deg, rgba(255,255,255,0) 60%, #fff 100%),
      linear-gradient(90deg, #a83038 0%, #c4575a 8%, #8d2530 14%, #e9e2e0 20%, #fff 40%, #fff 60%, #e8e2e0 80%, #b8343c 88%, #2a4e8a 100%);
  }
  .backdrop-sky {
    position: absolute; right: 0; top: 0; width: 200px; height: 140px;
    background: linear-gradient(200deg, var(--sky), rgba(29,79,143,0));
  }

  .page {
    position: absolute; left: 120px; top: 23px; width: 824px; height: 1177px;
    background: var(--page);
  }

  .brand { position: absolute; left: 25px; top: 22px; display: flex; align-items: center; gap: 12px; }
  .brand-mark { width: 44px; height: 44px; border-radius: 50%; background: var(--brand-blue); }
  .brand-name { font-family: "Mulish", sans-serif; font-weight: 800; font-size: 29px; color: var(--ink); letter-spacing: -0.5px; line-height: 1; }
  .brand-sub { font-family: "Mulish", sans-serif; font-weight: 400; font-size: 10px; letter-spacing: 2px; color: var(--ink); margin-top: 3px; text-align: right; }

  .header-contact { position: absolute; right: 188px; top: 34px; text-align: right; }
  .header-contact .label { font-family: "Mulish", sans-serif; font-size: 12px; color: var(--muted); letter-spacing: .5px; }
  .header-contact .phone { font-family: "Mulish", sans-serif; font-size: 23px; color: var(--ink); margin-top: 4px; }
  .header-contact .phone span { color: var(--accent-orange); }
  .header-agent {
    position: absolute; left: 718px; top: 4px; width: 90px; height: 104px;
    background: linear-gradient(180deg, #e8dcd2, #c9b6a6 60%, #f1f1f1);
    border-radius: 40px 40px 0 0;
  }

  .main-nav {
    position: absolute; left: 17px; top: 108px; width: 790px; height: 38px;
    border-radius: 4px; border: 1px solid var(--brand-blue-dark);
    background: linear-gradient(180deg, var(--brand-blue-light), var(--brand-blue) 55%, var(--brand-blue-dark));
    display: flex;
  }
  .main-nav a {
    font-family: "Cinzel", serif; font-size: 14.5px; color: #fff; text-decoration: none;
    display: flex; align-items: center; justify-content: center;
    border-right: 1px solid rgba(0,40,90,.45); box-shadow: 1px 0 0 rgba(255,255,255,.2);
  }
  .main-nav a:last-child { border-right: 0; box-shadow: none; }

  .hero {
    position: absolute; left: 16px; top: 163px; width: 792px; height: 438px;
    border: 1px solid var(--rule); border-radius: 4px; background: #fff; padding: 7px;
  }
  .hero-photo {
    position: relative; width: 100%; height: 100%;
    background:
      radial-gradient(ellipse at 70% 40%, #e7a07a 0%, rgba(231,160,122,0) 40%),
      linear-gradient(180deg, #6b3a2c 0%, #b85a4a 45%, #d24a5a 75%, #e03a5c 100%);
  }
  .hero-caption {
    position: absolute; left: 0; top: 270px; width: 482px; padding: 8px 17px;
    background: rgba(60,25,30,.62);
    font-family: "Mulish", sans-serif; font-weight: 700; font-size: 26px; line-height: 34px; color: #fff;
  }

  .welcome { position: absolute; left: 17px; top: 620px; }
  .welcome .lead { font-family: "Raleway", sans-serif; font-weight: 300; font-size: 32px; color: var(--ink-soft); line-height: 34px; }
  .welcome .name { font-family: "Cinzel", serif; font-size: 30px; color: var(--accent-orange); line-height: 34px; }

  .intro { position: absolute; left: 17px; top: 724px; width: 790px; font-size: 15px; line-height: 23px; color: var(--ink); }
  .intro p { margin-bottom: 20px; }
  .intro em { color: var(--brand-blue-dark); font-weight: 700; }

  .callout {
    position: absolute; left: 16px; top: 909px; width: 792px; height: 50px;
    border: 1px solid var(--rule); border-radius: 4px;
    background: linear-gradient(180deg, #fbfbfb, #ececec);
    display: flex; align-items: center; justify-content: space-between; padding: 0 24px;
    font-family: "Mulish", sans-serif; font-size: 12px; color: var(--ink);
  }
  .callout .tel { color: var(--accent-orange); margin: 0 4px; }
  .social { display: flex; gap: 5px; }
  .social span { width: 13px; height: 13px; background: var(--brand-blue); border-radius: 2px; }

  .footer-cols { position: absolute; left: 17px; top: 1002px; width: 790px; height: 110px; font-family: "Mulish", sans-serif; font-size: 12px; color: var(--ink-soft); }
  .footer-cols h3 { font-family: "Cinzel", serif; font-weight: 400; font-size: 15px; color: var(--brand-blue); margin-bottom: 10px; letter-spacing: .3px; }
  .footer-col { position: absolute; top: 0; }
  .footer-col ul { list-style: none; }
  .footer-col li { line-height: 20.5px; }
  .contact-info { left: 0; }
  .contact-info strong { font-weight: 700; }
  .contact-info .area { font-style: italic; font-size: 10.5px; }
  .quick-links { left: 244px; }
  .support { left: 587px; }
  .link-grid { display: grid; grid-template-columns: 160px 120px; }
  .support .link-grid { grid-template-columns: 95px 110px; }

  .legal { position: absolute; left: 17px; top: 1129px; width: 790px; border-top: 1px solid var(--rule); text-align: center; font-family: "Mulish", sans-serif; font-size: 12px; color: var(--muted); padding-top: 12px; line-height: 22px; }
  .legal a { color: var(--brand-blue-dark); text-decoration: none; }
</style>
</head>
<body>
<div class="canvas">
  <div class="backdrop" role="img" aria-label="Layered red and blue oriental rugs fanned out behind the page"></div>
  <div class="backdrop-sky"></div>

  <div class="page">
    <header>
      <div class="brand">
        <div class="brand-mark"></div>
        <div>
          <div class="brand-name">LoomRinsePro</div>
          <div class="brand-sub">HARBORFRESH CARE, LLC</div>
        </div>
      </div>
      <div class="header-contact">
        <div class="label">CONTACT US TODAY</div>
        <div class="phone"><span>(555).</span>014.2290</div>
      </div>
      <div class="header-agent" role="img" aria-label="Customer service agent with a headset"></div>
    </header>

    <nav class="main-nav">
      <a href="#" style="width:82px">HOME</a>
      <a href="#" style="width:101px">ABOUT US</a>
      <a href="#" style="width:134px">RUG WASHING</a>
      <a href="#" style="width:142px">WATER DAMAGE</a>
      <a href="#" style="width:158px">CARPET CLEANING</a>
      <a href="#" style="width:171px">CONTACT US</a>
    </nav>

    <section class="hero">
      <div class="hero-photo" role="img" aria-label="Technician vacuuming a red rug in a shop hung with oriental rugs and cushions">
        <div class="hero-caption">Professional Domestic Rug Cleaning<br>of Persain, Oriental &amp; Modern Rugs</div>
      </div>
    </section>

    <div class="welcome">
      <div class="lead">Welcome to</div>
      <div class="name">LOOM RINSE PRO</div>
    </div>

    <div class="intro">
      <p>When it comes to cleaning carpet, oriental rugs, area rugs or furniture ~ any fabric from antique silk brocades to contemporary carpet fibers ~ our service is unparalled.</p>
      <p>Harborfresh Care &amp; Restoration is the recipient of the 2010 &amp; 2011<br><em>"Best in Business Award" in Fernhollow,</em> Alabama for Water Damage Restoration and Carpet and Rug Cleaning.</p>
      <p>&nbsp;Please contact us for an extensive list of references.</p>
    </div>

    <div class="callout">
      <div><strong style="font-weight:400;color:#000">Not sure what you need?</strong> Call us at <span class="tel">(555) 014-2290</span> today!</div>
      <div class="social"><span></span><span></span><span></span><span></span></div>
    </div>

    <footer class="footer-cols">
      <div class="footer-col contact-info">
        <h3>CONTACT INFO</h3>
        <ul>
          <li><strong>Harborfresh Care &amp; Restoration</strong></li>
          <li>48 Quarry Lane</li>
          <li>Alderbrook, AL&nbsp; 35010</li>
          <li class="area">Serving Fernhollow and surrounding areas.</li>
        </ul>
      </div>
      <div class="footer-col quick-links">
        <h3>QUICK LINKS</h3>
        <ul class="link-grid">
          <li>Home</li><li>Water Damage</li>
          <li>About Us</li><li>Carpet Cleaning</li>
          <li>Rug Washing</li><li>Contact Us</li>
        </ul>
      </div>
      <div class="footer-col support">
        <h3>SUPPORT</h3>
        <ul class="link-grid">
          <li>Support</li><li>Privacy Policy</li>
          <li>FAQs</li><li>Terms &amp; Conditions</li>
          <li>Sitemap</li><li></li>
        </ul>
      </div>
    </footer>

    <div class="legal">
      © Copyright 2012 Loom Rinse Pro. All Rights Reserved.<br>
      Telephone: <a href="#">(555) 014-2290</a> &nbsp; E-mail: <a href="#">care@harborfreshcare.example</a>
    </div>
  </div>
</div>
</body>
</html>
```